Basic images needed for business powerpoint slides

We need basic images for a powerpoint design. The designs should be clean, modern, simple and easy to read on a screen and if they were printed on paper. The images should not be overly designed (no fancy graphics or ornate fonts), but should still look professional.

Please pay attention to the attachments that have sketches of the images that are needed. In the notes section of the powerpoint slides specifies additional details for each image.

Also, please adhere to the design guidelines that are also uploaded. Only use colors and fonts that are specified. The final images should be similar to the look and feel of the images in the design guidelines.
Updates

Designers -
Thanks for all your submissions! I am reviewing all the designs with my team and will have a decision ready by Sunday evening. If you are submitting any new designs, please submit by Sunday morning EST so my team can review them.

Thanks!

Target Market(s)

business executives

Industry/Entity Type

Business

Requirements
Must have
• Must Have:
- 1. Please see the attached powerpoint for the sketches we would like to have recreated. There are specific notes in each slide with additional details.

2. Please refer to the following pages in the uploaded design guideline document:
Colors - p. 14
- Use either the bright or muted color options as specified in the color scheme on this page

Typography - p. 16-17
- Use either helvetica or arial options

Powerpoint guidelines - p.42
- see for example of the general look and feel of the company

```html
<!DOCTYPE html>
<html lang="en">
<head>
<meta charset="utf-8">
<title>Team Structure Slides</title>
<link rel="stylesheet" href="https://fonts.googleapis.com/css2?family=Arimo:wght@400;700&display=swap">
<style>
  :root {
    --page: #ffffff;
    --slide: #e7e7e8;
    --strip: #f7941d;
    --orange: #f7941d;
    --ring-orange: #ef8a2e;
    --teal: #4fc3c3;
    --yellow: #ffcc05;
    --sky: #5bb5e6;
    --ink: #111111;
    --dark: #1a1a1a;
    --dim: #3a3a3a;
    --line: #1f5ba8;
    --cream: #fdf5d0;
  }
  html, body { margin: 0; padding: 0; overflow: hidden; background: var(--page); }
  .canvas { position: relative; width: 1200px; height: 918px; overflow: hidden; font-family: "Arimo", Arial, sans-serif; }
  .slide { position: absolute; width: 539px; height: 404px; background: var(--slide); }
  .slide svg { display: block; width: 539px; height: 404px; }
  .slide--org { left: 47px; top: 36px; }
  .slide--rings { left: 626px; top: 36px; }
  .slide--quad-a { left: 37px; top: 486px; }
  .slide--quad-b { left: 626px; top: 486px; }
  .strip { fill: var(--strip); }
  .connector { stroke: var(--line); stroke-width: 2.5; fill: none; }
  .divider { stroke: var(--line); stroke-width: 5; stroke-dasharray: 30 16; }
  .box-orange { fill: var(--orange); stroke: var(--line); stroke-width: 1.2; }
  .box-teal { fill: var(--teal); stroke: var(--line); stroke-width: 1.2; }
  .box-cream { fill: var(--cream); stroke: var(--line); stroke-width: 1.2; }
  .unit-title { font-size: 14px; font-weight: 700; fill: var(--ink); }
  .role { font-size: 9px; font-weight: 700; fill: var(--ink); }
  .person { font-size: 9px; fill: var(--ink); }
  .zone { font-size: 13px; font-weight: 700; fill: var(--ink); }
  .ring-outer { fill: var(--ring-orange); }
  .ring-mid { fill: var(--teal); }
  .ring-inner { fill: var(--yellow); }
  .seg-light { fill: var(--sky); stroke: #fff; stroke-width: 2.5; }
  .seg-dark { fill: var(--dark); stroke: #fff; stroke-width: 2.5; }
  .num { font-size: 14px; font-weight: 700; fill: var(--ink); }
  .num-dim { font-size: 14px; font-weight: 700; fill: var(--dim); }
  .label { font-size: 6.5px; fill: var(--ink); }
  .label-dim { font-size: 6px; fill: var(--dim); }
</style>
</head>
<body>
<div class="canvas">

  <!-- Organisation chart -->
  <div class="slide slide--org">
    <svg viewBox="0 0 539 404">
      <path class="connector" d="M33 91 V289 H48 M33 148 H48 M136 91 V148 H156"/>
      <path class="connector" d="M363 82 V290 H375 M451 82 V125 H461 M317 157 L340 124 H373"/>
      <line class="divider" x1="0" y1="247" x2="539" y2="247"/>

      <rect class="box-orange" x="33" y="44" width="147" height="47"/>
      <text class="unit-title" x="106" y="73" text-anchor="middle">Medical Products</text>

      <rect class="box-teal" x="361" y="34" width="150" height="48"/>
      <text class="unit-title" x="436" y="63" text-anchor="middle">Bio Science</text>

      <rect class="box-orange" x="48" y="124" width="80" height="48" rx="5"/>
      <text class="role" x="88" y="141" text-anchor="middle">Medical Affairs</text>
      <text class="person" x="88" y="153" text-anchor="middle">Marisa Doyle</text>
      <text class="person" x="88" y="165" text-anchor="middle">Helen Varga</text>

      <rect class="box-orange" x="156" y="129" width="64" height="39" rx="5"/>
      <text class="role" x="188" y="145" text-anchor="middle">Commercial</text>
      <text class="person" x="188" y="157" text-anchor="middle">Paula Grant</text>

      <rect class="box-teal" x="373" y="106" width="72" height="38" rx="5"/>
      <text class="role" x="409" y="122" text-anchor="middle">Medical Affairs</text>
      <text class="person" x="409" y="134" text-anchor="middle">Tomas Reyes</text>

      <rect class="box-teal" x="461" y="104" width="70" height="42" rx="5"/>
      <text class="role" x="496" y="117" text-anchor="middle">Commercial</text>
      <text class="person" x="496" y="129" text-anchor="middle">Nina Petrov</text>
      <text class="person" x="496" y="140" text-anchor="middle">Joanna Kerr</text>

      <rect class="box-teal" x="281" y="157" width="72" height="40" rx="5"/>
      <text class="role" x="317" y="173" text-anchor="middle">Clinical Trials</text>
      <text class="person" x="317" y="186" text-anchor="middle">Laura Benton</text>

      <rect class="box-orange" x="48" y="266" width="80" height="46" rx="5"/>
      <text class="role" x="88" y="281" text-anchor="middle">Medical Affairs</text>
      <text class="person" x="88" y="293" text-anchor="middle">Sandra Holt</text>
      <text class="person" x="88" y="305" text-anchor="middle">Ruth Ames</text>

      <text class="zone" x="253" y="299" text-anchor="middle">External</text>

      <rect class="box-teal" x="375" y="272" width="70" height="36" rx="5"/>
      <text class="role" x="410" y="287" text-anchor="middle">Medical Affairs</text>
      <text class="person" x="410" y="299" text-anchor="middle">Leila Haddad</text>

      <rect class="box-cream" x="204" y="334" width="89" height="51" rx="6"/>
      <text class="role" x="248" y="350" text-anchor="middle">Contributions</text>
      <text class="person" x="248" y="362" text-anchor="middle">Management Team</text>
      <text class="person" x="248" y="374" text-anchor="middle">Monica Faure</text>
    </svg>
  </div>

  <!-- Three-segment ring diagram -->
  <div class="slide slide--rings">
    <svg viewBox="0 0 539 404">
      <rect class="strip" x="0" y="0" width="42" height="404"/>
      <circle class="ring-outer" cx="212" cy="180" r="165"/>
      <circle class="ring-mid" cx="212" cy="180" r="135"/>
      <circle class="ring-inner" cx="212" cy="180" r="103"/>
      <path class="seg-light" d="M212 180 L212 105 A75 75 0 0 0 147 217.5 Z"/>
      <path class="seg-dark" d="M212 180 L212 105 A75 75 0 0 1 277 217.5 Z"/>
      <path class="seg-dark" d="M212 180 L277 217.5 A75 75 0 0 1 147 217.5 Z"/>

      <text class="num" x="188" y="38" text-anchor="end">15</text>
      <text class="label" x="217" y="27" text-anchor="middle">Franchise Lawyers</text>
      <text class="label" x="217" y="35" text-anchor="middle">Finance</text>
      <text class="label" x="217" y="43" text-anchor="middle">Committee Members</text>

      <text class="num" x="190" y="70" text-anchor="end">14</text>
      <text class="label" x="196" y="67">Legal Analysts</text>

      <text class="num" x="190" y="101" text-anchor="end">13</text>
      <text class="label" x="214" y="85" text-anchor="middle">Physicians</text>
      <text class="label" x="214" y="93" text-anchor="middle">Clinicians</text>
      <text class="label" x="214" y="101" text-anchor="middle">Scientists</text>

      <text class="num" x="178" y="151" text-anchor="middle">10</text>
      <text class="label" x="178" y="163" text-anchor="middle">HFAC specialists</text>
      <text class="label" x="178" y="171" text-anchor="middle">(Med Products –</text>
      <text class="label" x="178" y="179" text-anchor="middle">Med Affairs)</text>

      <text class="num-dim" x="246" y="151" text-anchor="middle">11</text>
      <text class="label-dim" x="248" y="163" text-anchor="middle">HFAC specialists</text>
      <text class="label-dim" x="248" y="171" text-anchor="middle">(Bio Science –</text>
      <text class="label-dim" x="248" y="179" text-anchor="middle">Med Affairs)</text>

      <text class="num-dim" x="212" y="213" text-anchor="middle">12</text>
      <text class="label-dim" x="212" y="222" text-anchor="middle">HFAC specialists</text>
      <text class="label-dim" x="212" y="229" text-anchor="middle">Contributions</text>
      <text class="label-dim" x="212" y="236" text-anchor="middle">Management</text>
      <text class="label-dim" x="212" y="243" text-anchor="middle">Program</text>

      <text class="label" x="212" y="268" text-anchor="middle">External Orgs</text>
    </svg>
  </div>

  <!-- Four-segment ring diagram, segment 1 highlighted -->
  <div class="slide slide--quad-a">
    <svg viewBox="0 0 539 404">
      <rect class="strip" x="0" y="0" width="41" height="404"/>
      <circle class="ring-outer" cx="210" cy="174" r="163"/>
      <circle class="ring-mid" cx="210" cy="174" r="133"/>
      <circle class="ring-inner" cx="210" cy="174" r="100"/>
      <path class="seg-light" d="M210 174 L138 174 A72 72 0 0 1 210 102 Z"/>
      <path class="seg-dark" d="M210 174 L210 102 A72 72 0 0 1 282 174 Z"/>
      <path class="seg-dark" d="M210 174 L282 174 A72 72 0 0 1 210 246 Z"/>
      <path class="seg-dark" d="M210 174 L210 246 A72 72 0 0 1 138 174 Z"/>

      <text class="num" x="198" y="39" text-anchor="end">9</text>
      <text class="label" x="204" y="30">Franchise Lawyers</text>
      <text class="label" x="214" y="38">Finance</text>
      <text class="num" x="198" y="70" text-anchor="end">8</text>
      <text class="label" x="204" y="67">Legal Analysts</text>
      <text class="num" x="198" y="100" text-anchor="end">7</text>
      <text class="label" x="204" y="97">Sales&amp;Marketing</text>

      <text class="num" x="151" y="155">1</text>
      <text class="label" x="160" y="150">HFAC specialists</text>
      <text class="label" x="160" y="158">(Med–Commercial</text>
      <text class="label" x="160" y="166">Products)</text>

      <text class="num-dim" x="214" y="155">2</text>
      <text class="label-dim" x="223" y="150">HFAC specialists</text>
      <text class="label-dim" x="223" y="158">(Med–Commercial</text>
      <text class="label-dim" x="223" y="166">Products)</text>

      <text class="num-dim" x="151" y="194">3</text>
      <text class="label-dim" x="160" y="186">HFAC specialists</text>
      <text class="label-dim" x="160" y="194">(Med Products –</text>
      <text class="label-dim" x="160" y="202">Med Affairs)</text>

      <text class="num-dim" x="214" y="194">4</text>
      <text class="label-dim" x="223" y="186">HFAC specialists</text>
      <text class="label-dim" x="223" y="194">(Bio Science –</text>
      <text class="label-dim" x="223" y="202">Med Affairs)</text>

      <text class="num-dim" x="214" y="224">5</text>
      <text class="label-dim" x="223" y="221">Clinical Trials</text>

      <text class="num" x="198" y="258" text-anchor="end">6</text>
      <text class="label" x="204" y="256">Scientists</text>
    </svg>
  </div>

  <!-- Four-segment ring diagram, segment 2 highlighted -->
  <div class="slide slide--quad-b">
    <svg viewBox="0 0 539 404">
      <rect class="strip" x="0" y="0" width="41" height="404"/>
      <circle class="ring-outer" cx="210" cy="174" r="163"/>
      <circle class="ring-mid" cx="210" cy="174" r="133"/>
      <circle class="ring-inner" cx="210" cy="174" r="100"/>
      <path class="seg-dark" d="M210 174 L138 174 A72 72 0 0 1 210 102 Z"/>
      <path class="seg-light" d="M210 174 L210 102 A72 72 0 0 1 282 174 Z"/>
      <path class="seg-dark" d="M210 174 L282 174 A72 72 0 0 1 210 246 Z"/>
      <path class="seg-dark" d="M210 174 L210 246 A72 72 0 0 1 138 174 Z"/>

      <text class="num" x="198" y="39" text-anchor="end">9</text>
      <text class="label" x="204" y="30">Franchise Lawyers</text>
      <text class="label" x="214" y="38">Finance</text>
      <text class="num" x="198" y="70" text-anchor="end">8</text>
      <text class="label" x="204" y="67">Legal Analysts</text>
      <text class="num" x="198" y="100" text-anchor="end">7</text>
      <text class="label" x="204" y="97">Sales&amp;Marketing</text>

      <text class="num-dim" x="151" y="155">1</text>
      <text class="label-dim" x="160" y="150">HFAC specialists</text>
      <text class="label-dim" x="160" y="158">(Med–Commercial</text>
      <text class="label-dim" x="160" y="166">Products)</text>

      <text class="num" x="214" y="155">2</text>
      <text class="label" x="223" y="150">HFAC specialists</text>
      <text class="label" x="223" y="158">(Med–Commercial</text>
      <text class="label" x="223" y="166">Products)</text>

      <text class="num-dim" x="151" y="194">3</text>
      <text class="label-dim" x="160" y="186">HFAC specialists</text>
      <text class="label-dim" x="160" y="194">(Med Products –</text>
      <text class="label-dim" x="160" y="202">Med Affairs)</text>

      <text class="num-dim" x="214" y="194">4</text>
      <text class="label-dim" x="223" y="186">HFAC specialists</text>
      <text class="label-dim" x="223" y="194">(Bio Science –</text>
      <text class="label-dim" x="223" y="202">Med Affairs)</text>

      <text class="num-dim" x="214" y="224">5</text>
      <text class="label-dim" x="223" y="221">Clinical Trials</text>

      <text class="num" x="198" y="258" text-anchor="end">6</text>
      <text class="label" x="204" y="256">Scientists</text>
    </svg>
  </div>

</div>
</body>
</html>
```